I m Looking to Demonstrate My Product Features via Design & Elements

My Dear Freinds,

I am looking to demonstrate the following features of my product via design & elements (for my Brindlemart listing)
https://www.brindlemart.example/dp/X72QP4LWZN/ref=kvt_h_3_u

1) Soft Touch - Skin Friendly Silky Soft Lining Inner Brushed Fleece

2) Stretchable - Four-way Stretch for Unrestricted Movement

3) Breathable - Moisture Control Odor Resistant

4) Quick-Drying - Sweat Wicking and Quick Dry Performance

5) Moisture-Wicking - Excellent Mobility and Moisture-Wicking

6) Heat Retention - Excellent Thermal Retention

7) Ultra-Light & Comfortable for Daily Warmth

8) Wonderfully Warm - Extra Layer of Warmth Under Your Clothes,

9) Elastic waistband - For the Pants for a Comfortable Snug Fit

10) Shrinkage Controlled - For lasting size and shape

see attached some examples & ideas

P.S. it shouldn't be exactly the same because these are from my competitors

Target Market(s)

People on Brindlemart who are looking to buy Thermal Underwear

Industry/Entity Type

Womens Clothing

Font styles to use
Serif

Colors

Designer to choose colors to be used in the design.

Requirements
Must have
• Needs to be attractive
Nice to have
• Ok
Should not have
• Ok

```html
<!DOCTYPE html>
<html lang="en">
<head>
<meta charset="utf-8">
<title>Thermal Set Features</title>
<link rel="stylesheet" href="https://fonts.googleapis.com/css2?family=Montserrat:wght@400;800&display=swap">
<style>
  :root {
    --paper: #fdfcf5;
    --ink: #1c1c1c;
    --icon: #3b2a80;
    --teal: #2a8aa6;
    --rug: #e4e6e6;
    --throw: #efece2;
  }
  html, body { margin: 0; padding: 0; overflow: hidden; }
  body { width: 1200px; height: 1200px; background: var(--paper); font-family: "Montserrat", sans-serif; color: var(--ink); }
  .canvas { position: relative; width: 1200px; height: 1200px; overflow: hidden; }
  .lifestyle-photo {
    position: absolute; left: 0; top: 262px; width: 1200px; height: 680px;
    background:
      radial-gradient(ellipse 26% 40% at 70% 38%, rgba(42,138,166,.85), rgba(42,138,166,0) 70%),
      radial-gradient(ellipse 38% 12% at 42% 70%, rgba(42,138,166,.8), rgba(42,138,166,0) 75%),
      radial-gradient(ellipse 18% 32% at 85% 55%, rgba(239,236,226,.95), rgba(239,236,226,0) 75%),
      radial-gradient(ellipse 60% 22% at 50% 82%, var(--rug), rgba(228,230,230,0) 75%);
  }
  .feature { position: absolute; width: 240px; text-align: center; }
  .feature svg { display: block; margin: 0 auto 12px; width: 72px; height: 72px; }
  .feature svg * { fill: none; stroke: var(--icon); stroke-width: 2.6; stroke-linecap: round; stroke-linejoin: round; }
  .feature svg .solid { fill: var(--icon); stroke: none; }
  .feature-title { margin: 0; font-weight: 800; font-size: 17.5px; line-height: 20px; }
  .feature-text { margin: 0; font-weight: 400; font-size: 15.5px; line-height: 19.5px; letter-spacing: .3px; }
  .top { top: 80px; }
  .bottom { top: 958px; }
</style>
</head>
<body>
<div class="canvas">
  <div class="lifestyle-photo" role="img" aria-label="Woman in a teal thermal top and leggings reclining on a white shaggy rug with a cream throw and an open book"></div>

  <div class="feature top" style="left:25px">
    <svg viewBox="0 0 72 72"><path d="M30 2l6 6 6-6"/><path d="M14 30l-6 6 6 6M58 30l6 6-6 6"/><circle cx="36" cy="34" r="16"/><path class="solid" d="M32 30a4 4 0 0 1 8 0v12l10 2c3 1 4 3 3 6l-3 14H30l-8-14c-1-3 2-5 5-3l5 4z"/></svg>
    <p class="feature-title">Soft Touch</p>
    <p class="feature-text">Skin Friendly Silky<br>Soft Lining<br>Inner Brushed<br>Fleece</p>
  </div>
  <div class="feature top" style="left:256px">
    <svg viewBox="0 0 72 72"><path d="M8 18h56M8 30h56M8 42h56M8 54h56M18 8v56M30 8v56M42 8v56M54 8v56"/><rect x="12" y="12" width="48" height="48" rx="6"/></svg>
    <p class="feature-title">Stretchable</p>
    <p class="feature-text">Four-way Stretch for<br>Unrestricted Movement</p>
  </div>
  <div class="feature top" style="left:478px">
    <svg viewBox="0 0 72 72"><path d="M36 6v30M36 30l-10 8M36 30l10 8"/><path d="M28 22c-12 0-18 18-18 34 0 6 6 6 18 0V22zM44 22c12 0 18 18 18 34 0 6-6 6-18 0V22z"/></svg>
    <p class="feature-title">Breathable</p>
    <p class="feature-text">Moisture Control<br>Odor Resistant</p>
  </div>
  <div class="feature top" style="left:703px">
    <svg viewBox="0 0 72 72"><circle cx="32" cy="30" r="22"/><path d="M22 30h40v24a6 6 0 0 1-6 6H28a6 6 0 0 1-6-6z"/><path d="M26 36h32"/><path d="M30 28c0-6 8-8 10-4 3-4 12-2 11 4"/></svg>
    <p class="feature-title">Moisture-Wicking</p>
    <p class="feature-text">Excellent Mobility<br>and Moisture-Wicking</p>
  </div>
  <div class="feature top" style="left:942px">
    <svg viewBox="0 0 72 72"><path d="M32 10a4 4 0 1 1 4 4v4"/><path class="solid" d="M20 24l14-4 14 4 4 14-6 2v16H22V40l-6-2z"/><path d="M46 46h18M46 52h18M46 58h18M46 64h18"/><path d="M60 6v6M57 9h6M10 56v6M7 59h6"/></svg>
    <p class="feature-title">Quick-Drying</p>
    <p class="feature-text">Sweat Wicking and<br>Quick Dry<br>Performance</p>
  </div>

  <div class="feature bottom" style="left:27px">
    <svg viewBox="0 0 72 72"><path d="M22 8a6 6 0 0 1 12 0v42a12 12 0 1 1-12 0z"/><path d="M28 20v34"/><circle cx="28" cy="58" r="6" class="solid"/><circle cx="50" cy="14" r="6"/><path d="M50 4v3M50 21v3M40 14h3M57 14h3"/></svg>
    <p class="feature-title">Heat Retention</p>
    <p class="feature-text">Excellent Thermal<br>Retention</p>
  </div>
  <div class="feature bottom" style="left:255px">
    <svg viewBox="0 0 72 72"><path d="M36 46l-10-10a6 6 0 0 1 10-7 6 6 0 0 1 10 7z"/><path d="M20 14c6-6 22-8 30-2l8 6h10v14"/><path d="M52 58c-6 6-22 8-30 2l-8-6H4V40"/><path d="M18 22a20 20 0 0 0-4 10M54 50a20 20 0 0 0 4-10" stroke-dasharray="2 5"/></svg>
    <p class="feature-title">Ultra-Light</p>
    <p class="feature-text">Comfortable for<br>Daily Warmth</p>
  </div>
  <div class="feature bottom" style="left:478px">
    <svg viewBox="0 0 72 72"><circle cx="36" cy="36" r="18"/><path d="M36 6v10M36 56v10M6 36h10M56 36h10M15 15l7 7M50 50l7 7M57 15l-7 7M22 50l-7 7"/></svg>
    <p class="feature-title">Wonderfully Warm</p>
    <p class="feature-text">Extra Layer of Warmth<br>Under Your Clothes,</p>
  </div>
  <div class="feature bottom" style="left:703px">
    <svg viewBox="0 0 72 72"><path d="M4 28c20 10 44 10 64 0M4 44c20-10 44-10 64 0"/><path d="M32 4h8v14h6L36 28 26 18h6zM32 68h8V54h6L36 44 26 54h6z"/><path d="M14 36h44" stroke-dasharray="4 6"/></svg>
    <p class="feature-title">Elastic waistband</p>
    <p class="feature-text">For the Pants for a<br>Comfortable Snug Fit</p>
  </div>
  <div class="feature bottom" style="left:942px">
    <svg viewBox="0 0 72 72"><path d="M36 4v20M28 16l8 8 8-8M36 68V48M28 56l8-8 8 8"/><path d="M4 30h64M4 42h64" stroke-width="3.4"/><path d="M4 36h6M14 36h4M56 36h4M64 36h4"/></svg>
    <p class="feature-title">Shrinkage Controlled</p>
    <p class="feature-text">For lasting size<br>and shape</p>
  </div>
</div>
</body>
</html>
```